Stonefield Partners Business Card Design

We are looking for a new business card design, we are not happy with our current design. We are a boutique management consulting firm and our clients are typically fortune 500 companies.

I have attached the current front and back that we have as well as a version of our logo that can be used. I am trying to get a higher resolution version of the logo file to upload to the project.

Target Market(s)

Fortune 500 companies are our primary client base. Financial services, life sciences, pharmaceuticals and telecom companies are

Industry/Entity Type

Management Consulting

Contact Information for Business Card

We are trying to communicate a high degree of professionalism, a somewhat minimalist perhaps with some air of whimsy (without overdoing it). Attached is the current design, front and back as well as logos. I like the current back of the card and assume we will keep the phrase the same.

From a color palette perspective, I prefer to stay with a gray scale as they are today.

Font styles to use
Sans Serif

Colors
1b1b1b
474747
ffffff

Requirements
Must have
• Two sided business card design. File format should be something that can be used outside of Photoshop like MS Publisher so that they can be edited with personal information.
• Font should be calibri or something very similar and should be available within MS Office
Should not have
• No other logos or graphics outside of the logo provided.

```html
<!DOCTYPE html>
<html lang="en">
<head>
<meta charset="utf-8">
<title>Stonefield Partners Business Card</title>
<link rel="stylesheet" href="https://fonts.googleapis.com/css2?family=Carlito:wght@400;700&display=swap">
<style>
  :root {
    --ink: #1b1b1b;
    --slate: #474747;
    --paper: #ffffff;
    --backdrop: #e9eaec;
    --card-w: 640px;
    --card-h: 366px;
  }
  * { box-sizing: border-box; margin: 0; padding: 0; }
  html, body {
    width: 1200px;
    height: 900px;
    overflow: hidden;
  }
  body {
    background: var(--backdrop);
    font-family: "Carlito", "Calibri", sans-serif;
    color: var(--ink);
    position: relative;
  }
  .card {
    position: absolute;
    left: 280px;
    width: var(--card-w);
    height: var(--card-h);
    background: var(--paper);
    box-shadow: 0 6px 18px rgba(0,0,0,0.12);
    overflow: hidden;
  }
  .card--front { top: 50px; }
  .card--back { top: 476px; }

  /* Front */
  .front-header {
    height: 150px;
    display: flex;
    justify-content: space-between;
    padding: 18px 26px 0 56px;
  }
  .brand-mark {
    display: flex;
    align-items: center;
    gap: 12px;
    height: 112px;
    font-weight: 700;
    font-size: 30px;
    color: var(--ink);
  }
  .brand-dot {
    width: 30px;
    height: 30px;
    border-radius: 50%;
    background: var(--ink);
  }
  .holder {
    text-align: center;
    width: 300px;
  }
  .holder-name {
    font-size: 44px;
    line-height: 1;
    margin-bottom: 20px;
    letter-spacing: 0.5px;
  }
  .holder-name strong { font-weight: 700; }
  .holder-name span { font-weight: 400; }
  .holder-line {
    font-size: 19px;
    line-height: 1.2;
  }
  .holder-line--firm { font-weight: 700; }

  .front-bands {
    display: flex;
    height: calc(var(--card-h) - 150px);
  }
  .band {
    flex: 1;
    color: var(--paper);
    text-align: center;
    font-size: 20px;
    line-height: 1.3;
    letter-spacing: 0.4px;
  }
  .band--address {
    background: var(--slate);
    padding-top: 12px;
    border-right: 2px solid var(--paper);
  }
  .band--contact {
    background: var(--ink);
    padding-top: 22px;
  }
  .band strong { font-weight: 700; }

  /* Back */
  .card--back {
    display: flex;
    flex-direction: column;
    align-items: center;
    justify-content: center;
  }
  .wordmark {
    display: flex;
    align-items: center;
    gap: 16px;
    font-weight: 700;
    font-size: 80px;
    line-height: 1;
    color: var(--ink);
    margin-bottom: 42px;
  }
  .wordmark .brand-dot {
    width: 58px;
    height: 58px;
  }
  .wordmark sup {
    font-size: 16px;
    font-weight: 700;
    align-self: flex-start;
    margin-left: -10px;
  }
  .tagline {
    text-align: center;
    font-size: 30px;
    line-height: 1.3;
  }
</style>
</head>
<body>

  <section class="card card--front">
    <header class="front-header">
      <div class="brand-mark">
        <span class="brand-dot"></span>
        <span class="brand-name">Stonefield</span>
      </div>
      <div class="holder">
        <h1 class="holder-name"><strong>Daniel</strong><span>Hart</span></h1>
        <p class="holder-line">Los Angeles Office</p>
        <p class="holder-line">Managing Director</p>
        <p class="holder-line holder-line--firm">Stonefield Partners, Inc.</p>
      </div>
    </header>
    <div class="front-bands">
      <address class="band band--address" style="font-style:normal">
        <strong>Stonefield Partners, Inc.</strong><br>
        Headquarters<br>
        218 Harlow Street<br>
        Suite 210<br>
        Cedar Bay, WA 98421
      </address>
      <div class="band band--contact">
        206.555.0142<br>
        dhart@stonefieldpartners.com<br>
        <strong>www.StonefieldPartners.com</strong>
      </div>
    </div>
  </section>

  <section class="card card--back">
    <div class="wordmark">
      <span class="brand-dot"></span>
      <span class="brand-name">Stonefield</span>
      <sup>TM</sup>
    </div>
    <p class="tagline">The preferred choice<br>for leadership’s top priorities</p>
  </section>

</body>
</html>
```